bramblecrest paving card makeover

were a excavation/paving contractor from Monterey ca, I'm looking to have a card designed front and back that has company details on the front and a list of the services we offer on the back.

Target Market(s)

home owners property management companies

Industry/Entity Type

Contractor

Contact Information for Business Card

bramblecrest paving 418 larkmoor st Monterey ca. licensed, insured and bonded
lic#657920 gerald pinsky operations manager

Font styles to use
Serif
Sans Serif

Colors
f78f20

Requirements
Must have
• a list of my services on back, asphalt construction and maintenance, drainage, foundations, retaining walls, chip seals, excavation, grading, landscape ground work, interlocking paver, hydro-seeding, structured and driveway demolition, utility trenching and stump removal.
Nice to have
• my new domain and page address I'm acquiring from pixel bazaar.

```html
<!DOCTYPE html>
<html lang="en">
<head>
<meta charset="utf-8">
<title>Bramblecrest Paving – Business Card</title>
<link rel="stylesheet" href="https://fonts.googleapis.com/css2?family=Oswald:wght@400;500;600&display=swap">
<style>
  :root {
    --bg: #e9e4dc;
    --card-black: #0b0b0c;
    --asphalt-dark: #141414;
    --asphalt-mid: #262626;
    --orange: #f78f20;
    --white: #ffffff;
    --grey-text: #e6e6e6;
  }
  * { box-sizing: border-box; margin: 0; padding: 0; }
  html, body { width: 1200px; height: 800px; overflow: hidden; }
  body {
    background: var(--bg);
    font-family: "Oswald", "Arial Narrow", sans-serif;
    position: relative;
  }
  .card {
    position: absolute;
    top: 250px;
    width: 520px;
    height: 300px;
    border-radius: 4px;
    overflow: hidden;
    box-shadow: 0 6px 18px rgba(0,0,0,0.25);
  }
  .card-front { left: 60px; background: var(--card-black); }
  .card-back {
    left: 620px;
    background: radial-gradient(ellipse at 60% 40%, var(--asphalt-mid), var(--asphalt-dark) 75%);
  }
  .accent-bands { position: absolute; inset: 0; width: 100%; height: 100%; }

  .contact {
    position: absolute;
    left: 34px;
    top: 86px;
    color: var(--grey-text);
  }
  .contact-name {
    color: var(--orange);
    font-size: 27px;
    font-weight: 500;
    letter-spacing: 0.5px;
    line-height: 1;
  }
  .contact-role {
    font-size: 15px;
    letter-spacing: 1px;
    margin-top: 6px;
  }
  .contact-address {
    margin-top: 22px;
    font-size: 15px;
    line-height: 1.45;
  }
  .contact-lines {
    margin-top: 22px;
    font-size: 14px;
    line-height: 1.5;
    letter-spacing: 0.3px;
  }

  .brand-mark {
    position: absolute;
    display: flex;
    flex-direction: column;
    align-items: center;
    gap: 10px;
  }
  .brand-mark .brand-dot {
    width: 34px; height: 34px;
    border-radius: 50%;
    border: 3px solid var(--white);
  }
  .brand-mark .brand-name {
    color: var(--white);
    font-weight: 600;
    text-transform: uppercase;
    text-align: center;
    letter-spacing: 1.5px;
    line-height: 1.15;
  }
  .card-front .brand-mark { right: 40px; top: 40px; width: 190px; }
  .card-front .brand-name { font-size: 19px; }
  .card-back .brand-mark { right: 36px; top: 82px; width: 220px; }
  .card-back .brand-name { font-size: 22px; }

  .license {
    position: absolute;
    right: 28px;
    top: 214px;
    text-align: left;
    font-size: 14px;
    line-height: 1.35;
    color: var(--grey-text);
  }
  .license-number { color: var(--orange); }

  .services {
    position: absolute;
    left: 26px;
    top: 24px;
    list-style: none;
    color: var(--white);
    font-size: 13.5px;
    line-height: 1;
  }
  .services li {
    display: flex;
    align-items: center;
    height: 21.4px;
  }
  .services li::before {
    content: "";
    width: 12px;
    height: 10px;
    margin-right: 12px;
    background: var(--orange);
    border-radius: 0 6px 6px 0;
    flex: none;
  }
</style>
</head>
<body>

  <section class="card card-front" aria-label="Business card front">
    <svg class="accent-bands" viewBox="0 0 520 300" aria-hidden="true">
      <polygon points="0,52 210,52 196,66 0,66" fill="var(--orange)"/>
      <polygon points="330,282 520,282 520,296 316,296" fill="var(--orange)"/>
    </svg>

    <div class="contact">
      <p class="contact-name">DALE RENNER</p>
      <p class="contact-role">MANAGER</p>
      <p class="contact-address">Bramblecrest Paving<br>418 Larkmoor St Monterey CA</p>
      <p class="contact-lines">
        +1 555 014 2290<br>
        EMAIL@BRAMBLECRESTMAIL.COM<br>
        WWW.BRAMBLECRESTPAVING.COM
      </p>
    </div>

    <div class="brand-mark">
      <span class="brand-dot"></span>
      <span class="brand-name">Bramblecrest Paving And Concrete</span>
    </div>

    <p class="license">
      <span class="license-number">Lic#657920</span><br>
      Insured And Bonded
    </p>
  </section>

  <section class="card card-back" aria-label="Business card back">
    <ul class="services">
      <li>Asphalt Construction And Maintenance</li>
      <li>Drainage</li>
      <li>Foundations</li>
      <li>Retaining Walls</li>
      <li>Chip Seals</li>
      <li>Excavation Grading</li>
      <li>Landscape Ground Work</li>
      <li>Hydro-seeding</li>
      <li>Interlocking Paver</li>
      <li>Structured And Driveway Demolition</li>
      <li>Utility Trenching And Stump Removal</li>
    </ul>

    <div class="brand-mark">
      <span class="brand-dot"></span>
      <span class="brand-name">Bramblecrest Paving And Concrete</span>
    </div>
  </section>

</body>
</html>
```